Rug Cleaning Web Design Project

We need a web design for our cleaning company. We currently have a web page but are not happy with its design. We currently offer fine rug cleaning,upholstery cleaning, and residential and commercial carpet cleanning. We also offer water damage restoration. For our rug cleaning services we offer : Enzyme treatments for pet contamination and odor removal, application of stain protection that is designed for the fine textiles used in rug construction, application of treatments designed to prevent moth damage and pads designed to be used under rugs.Our current web site is harborfreshcare.example. We are intrested in a design with similar information to the web page of Velmora Rug Cleaners INC. We would like to use the colors that are present in our logo that will be uploaded with this description. We would also like this new page to be linked to our other address loomrinsepro.example. We would like the deign to be visually attractive but not "too busy".
Updates

Please include pictures of rugs, or people washing rugs if possible. We do not offer maid type cleaning services. We would not be interested in designs including pictures depicting that type service. Thanks for your hard work on this project.

Dana Whitlow

Industry/Entity Type

Residential

Requirements
Must have
• This page must be viewable on smart phones and tablets.

```html
<!DOCTYPE html>
<html lang="en">
<head>
<meta charset="utf-8">
<meta name="viewport" content="width=device-width, initial-scale=1">
<title>LoomRinsePro – Harborfresh Cleaning</title>
<link rel="stylesheet" href="https://fonts.googleapis.com/css2?family=Arimo:wght@400;700&display=swap">
<style>
:root{
  --blue:#0a5aa8;
  --blue-dark:#0b3f7c;
  --blue-light:#2a7fd0;
  --heading:#0d4f94;
  --ink:#333;
  --muted:#555;
  --page:#f7f5f7;
  --rule:#d6d6d6;
  --footer:#000;
  --footer-bar:#161616;
  --footer-text:#a8a8a8;
  --accent:#3ab0e6;
}
*{box-sizing:border-box;margin:0;padding:0}
html,body{width:1200px;height:1178px;overflow:hidden}
body{background:var(--page);font-family:"Arimo",Arial,sans-serif;color:var(--ink);position:relative}
.abs{position:absolute}
a{color:inherit;text-decoration:none}

/* header */
.brand{left:110px;top:10px;display:flex;align-items:center;gap:14px}
.brand-dot{width:50px;height:50px;border-radius:50%;background:var(--blue)}
.brand-name{font-size:34px;font-weight:700;color:#222;letter-spacing:-1px}
.toplinks{right:110px;top:6px;font-size:12.5px;color:#444;display:flex;gap:8px;align-items:center;letter-spacing:.5px}
.flag{width:16px;height:11px;background:linear-gradient(#c33 0 50%,#fff 50% 100%);border:1px solid #999;position:relative}
.flag::before{content:"";position:absolute;left:0;top:0;width:7px;height:6px;background:#2a4a9a}
.search{left:878px;top:54px;width:212px;height:25px;border:1px solid #bbb;border-radius:13px;background:#fff;font-size:12.5px;font-style:italic;color:#555;padding:5px 12px;letter-spacing:.5px}
.search svg{position:absolute;right:10px;top:5px}

/* nav */
.nav{left:110px;top:92px;width:980px;height:34px;border-radius:3px;background:linear-gradient(#1d6fc2,#0a4f99);display:flex}
.nav a{color:#fff;font-size:15px;display:flex;align-items:center;justify-content:center;border-right:1px solid #08386e;box-shadow:inset -1px 0 #2e80cf;letter-spacing:.3px}
.nav a:last-child{border:none;box-shadow:none;flex:1}

/* hero */
.hero{left:110px;top:139px;width:980px;height:323px;border-radius:3px;background:
  radial-gradient(ellipse at 70% 40%,#6f86a3 0 18%,transparent 40%),
  linear-gradient(100deg,#c0623a,#d8a07a 30%,#9e4a2c 55%,#c98a62 80%,#e0b899)}
.hero-panel{left:143px;top:170px;width:460px;height:148px;background:rgba(40,40,40,.72);border:5px solid rgba(120,120,120,.35)}
.hero-title{left:166px;top:186px;width:420px;color:#fff;font-size:16.5px;font-weight:700;line-height:22px;letter-spacing:.6px}
.btn{background:linear-gradient(#2a7fd0,#0b4f9a);color:#fff;border:1px solid #093f7a;border-radius:3px;display:flex;align-items:center;justify-content:center}
.hero-btn{left:168px;top:266px;width:104px;height:35px;font-size:15px}
.dots{left:524px;top:279px;display:flex;gap:3px}
.dots span{width:9px;height:9px;border-radius:50%;background:#555}
.dots span:first-child{background:#f08a1c}

/* overview */
.section-title{color:var(--heading);font-weight:700;letter-spacing:1.5px}
.overview-title{left:110px;top:497px;font-size:22px}
.overview-rule{left:110px;top:524px;width:690px;height:1px;background:var(--rule)}
.overview-lead{left:110px;top:538px;width:700px;font-size:13px;line-height:18px;letter-spacing:.5px;color:#333}
.overview-body{left:110px;top:583px;width:700px;font-size:12px;line-height:20px;color:var(--muted)}

/* quote */
.quote{left:843px;top:501px;width:247px;height:158px;background:#ececec;border:1px solid #d0d0d0;border-radius:3px}
.quote-head{left:843px;top:501px;width:247px;height:38px;background:linear-gradient(#1e6fc0,#0a4c95);border-radius:3px 3px 0 0;color:#fff;font-weight:700;font-size:18px;display:flex;align-items:center;justify-content:center;letter-spacing:.3px}
.quote-text{left:843px;top:546px;width:247px;text-align:center;font-size:13px;line-height:16px;color:#444;letter-spacing:.8px}
.quote-input{left:860px;top:587px;width:216px;height:24px;background:#fff;border:1px solid #bbb}
.quote-btn{left:995px;top:620px;width:81px;height:25px;font-size:12px;font-weight:700;letter-spacing:1px}

.divider{left:110px;top:701px;width:980px;height:1px;background:var(--rule)}

/* services */
.service{top:726px;width:227px}
.service h3{font-size:15.5px;color:var(--heading);font-weight:700;letter-spacing:1.3px;height:29px}
.service .photo{height:114px;border:1px solid #ccc}
.service p{margin-top:13px;font-size:12px;line-height:17px;color:#333}
.service .btn{position:absolute;right:0;top:214px;width:83px;height:25px;font-size:12.5px}

/* footer */
.footer{left:0;top:1000px;width:1200px;height:143px;background:var(--footer)}
.footer-bar{left:0;top:1143px;width:1200px;height:35px;background:var(--footer-bar)}
.footer h4{color:#fff;font-size:15px;letter-spacing:1.3px;font-weight:700}
.contact{left:110px;top:1021px;font-size:12.5px;color:var(--footer-text);line-height:17.5px}
.contact h4{margin-bottom:10px}
.contact .row{display:flex;align-items:center;gap:8px}
.contact .phone{font-style:italic;font-size:14px}
.links{left:400px;top:1021px}
.links ul{list-style:none;position:absolute;top:28px;font-size:12.5px;line-height:17px;color:var(--footer-text);white-space:nowrap}
.follow{right:110px;top:1024px;color:var(--accent);font-size:13px;letter-spacing:.3px}
.feed{left:711px;top:1044px;width:379px;height:71px;background:#1e1e1e;border-radius:3px;color:#777;font-size:12px;line-height:16px;padding:9px 13px}
.copyright{left:110px;top:1153px;color:#777;font-size:12.5px;letter-spacing:.5px}
.foot-brand{right:110px;top:1152px;display:flex;align-items:center;gap:5px;color:#555;font-size:12px;font-weight:700}
.foot-brand span{width:12px;height:12px;border-radius:50%;background:#444}
</style>
</head>
<body>

<header>
  <div class="abs brand"><span class="brand-dot"></span><span class="brand-name">LoomRinsePro</span></div>
  <div class="abs toplinks"><span class="flag"></span><span>English ▾</span><span>|</span><a href="#">Login</a><span>|</span><a href="#">Register</a></div>
  <div class="abs search">Search
    <svg width="12" height="12" viewBox="0 0 12 12"><circle cx="5" cy="5" r="3.5" fill="none" stroke="#888" stroke-width="1.4"/><line x1="7.5" y1="7.5" x2="11" y2="11" stroke="#888" stroke-width="1.6"/></svg>
  </div>
  <nav class="abs nav">
    <a href="#" style="width:101px">Home</a>
    <a href="#" style="width:125px">About Us</a>
    <a href="#" style="width:152px">Our Services</a>
    <a href="#" style="width:203px">Request an Estimate</a>
    <a href="#" style="width:133px">Our Location</a>
    <a href="#" style="width:129px">Web Links</a>
    <a href="#">Contact Us</a>
  </nav>
</header>

<section>
  <div class="abs hero" role="img" aria-label="Vacuum cleaner head gliding over a red and orange oriental rug"></div>
  <div class="abs hero-panel"></div>
  <h1 class="abs hero-title">WE OFFER FINE RUG CLEANING, UPHOLSTERY CLEANING, AND RESIDENTIAL AND COMMERCIAL CARPET CLEANNING...</h1>
  <a href="#" class="abs btn hero-btn">Read More</a>
  <div class="abs dots"><span></span><span></span><span></span><span></span></div>
</section>

<section>
  <h2 class="abs section-title overview-title">OVERVIEW</h2>
  <div class="abs overview-rule"></div>
  <p class="abs overview-lead">When it comes to cleaning carpet, oriental rugs, area rugs or furniture. any fabric from antique silk brocades to contemporary carpet fibers. our service is unparalled.</p>
  <p class="abs overview-body">Lorem ipsum dolor sit amet, consectetuer adipiscing elit, sed diam nonummy nibh euismod tincidunt ut laoreet dolore magna aliquam erat volutpat. Ut wisi enim ad minim veniam, quis nostrud exerci tation ullamcorper suscipit lobortis nisl ut aliquip ex ea commodo consequat. Duis autem vel eum iriure dolor in hendrerit in vulputate velit esse molestie consequat, vel illum dolore eu feugiat nulla facilisis at vero eros et accumsan et iusto odio dignissim</p>

  <div class="abs quote"></div>
  <div class="abs quote-head">OBTAIN A FREE QUOTE</div>
  <p class="abs quote-text">To book an appointment simply<br>enter your postcode.</p>
  <div class="abs quote-input"></div>
  <a href="#" class="abs btn quote-btn">SUBMIT</a>
</section>

<div class="abs divider"></div>

<section>
  <article class="abs service" style="left:110px">
    <h3>CARPET CLEANING</h3>
    <div class="photo" role="img" aria-label="Carpet cleaning wand on a cream carpet" style="background:linear-gradient(#8a8a6a,#d9d6cf 45%,#c9c5bd)"></div>
    <p>Lorem ipsum dolor sit amet, consectetuer adipiscing elit, sed diam nonummy nibh euismod</p>
    <a href="#" class="btn">Read more</a>
  </article>
  <article class="abs service" style="left:361px">
    <h3>PET ODOR REMOVAL</h3>
    <div class="photo" role="img" aria-label="Small dog resting on a rug" style="background:linear-gradient(#e8e6e2,#d8d2c8 60%,#b88a5a)"></div>
    <p>Lorem ipsum dolor sit amet, consectetuer adipiscing elit, sed diam nonummy nibh euismod</p>
    <a href="#" class="btn">Read more</a>
  </article>
  <article class="abs service" style="left:612px">
    <h3>UPHOLSTERY CLEANING</h3>
    <div class="photo" role="img" aria-label="Blue upholstered sofa in a bright living room" style="background:linear-gradient(#e6e2d8,#c8c2b4 40%,#6f86ad 65%,#4d6a98)"></div>
    <p>Lorem ipsum dolor sit amet, consectetuer adipiscing elit, sed diam nonummy nibh euismod</p>
    <a href="#" class="btn">Read more</a>
  </article>
  <article class="abs service" style="left:863px">
    <h3>FINE RUG CLEANING</h3>
    <div class="photo" role="img" aria-label="Stack of patterned fine rugs" style="background:linear-gradient(120deg,#8a5a2a,#c9a86a 40%,#2f3d55 70%,#a0642e)"></div>
    <p>Lorem ipsum dolor sit amet, consectetuer adipiscing elit, sed diam nonummy nibh euismod</p>
    <a href="#" class="btn">Read more</a>
  </article>
</section>

<footer>
  <div class="abs footer"></div>
  <div class="abs footer-bar"></div>
  <div class="abs contact">
    <h4>CONTACT US</h4>
    <div>Harborfresh Cleaning &amp; Restoration</div>
    <div>84 Linden Hollow Road Maplecrest, AL 35000</div>
    <div class="row"><svg width="13" height="9" viewBox="0 0 13 9"><rect x=".5" y=".5" width="12" height="8" fill="#888"/><path d="M.5 .5 6.5 5 12.5 .5" fill="none" stroke="#333"/></svg>care@harborfreshcare.example</div>
    <div class="row phone"><svg width="13" height="10" viewBox="0 0 13 10"><path d="M1 3Q6.5-1 12 3L11 5 9 4V3H4V4L2 5Z M3 6H10V10H3Z" fill="#888"/></svg>(555) 014-2277</div>
  </div>
  <div class="abs links">
    <h4>OTHER LINKS</h4>
    <ul style="left:2px"><li>Home</li><li>About Us</li><li>Our Services</li><li>Request an Estimate</li></ul>
    <ul style="left:160px"><li>Web Links</li><li>Our Location</li><li>Contact Us</li></ul>
  </div>
  <div class="abs follow">Follow us on our feed</div>
  <p class="abs feed">Lorem ipsum dolor sit amet, consectetuer adipiscing elit, sed diam nonummy nibh euismod tincidunt ut laoreet dolore magna aliquam erat volutpat. Ut wisi enim ad minim veniam.</p>
  <div class="abs copyright">© 2012 LoomRinsePro. All rights reserved</div>
  <div class="abs foot-brand"><span></span>LoomRinsePro</div>
</footer>

</body>
</html>
```